Calendar Design Project: 2025 with Specific Edits

This is a straightforward project where your creativity can shine!
Simply take the existing 2024 calendar and adapt it for 2025 by incorporating the new photos I've attached.
Please keep the overall concept of the 2024 calendar intact—your focus will be on enhancing it with fresh visuals.

I can't wait to see your amazing designs!
I am looking for a talented graphic designer to create a new 2025 calendar with specific adjustments.
Pictures attached.
Requirements:
Calendar Size: 52cm x 34cm
March Folder:
Adjust the image named "attached - DJI-0025" to make the circular road darker to match the rest of the design.
May Folder:
Modify the circled area in the May image to ensure it looks consistent with the other road (reference file: "attached - After").
November Folder:
Clear out the circled area in the November image (reference file: "attached - After1").
Please let me know if you have any questions or need further clarification.
I added to my breif a design i made last year for same client.
2025, calendar should be vertical and not horizontal. and some of the photos attache are "Before" and "After" please include together inside each month of the calendar.
Thank you!
Feel free to adjust any details as necessary!

Hello talented designers!

I’m excited to share that this is my 14th project on the ArtHarbor platform, and I’ve been fortunate to have successful collaborations in the past. I'm looking forward to creating a new 2025 calendar with your help, and I believe that with your creativity and skills, we can make this project a success as well!

I hope to establish a long-term relationship with a talented team like yours. As an added incentive, I will be offering a bonus for the winner, and I may select more than one winner, so everyone has a chance to shine!

Let’s make something amazing together!

Best
Update:
cancel or before, only place the After picture

Requirements
Must have
• Project Overview Objective: Create a 2025 calendar using the provided images, maintaining the design concept from the 2024 calendar but enhancing it with new visuals. Format: Vertical layout (52cm x 34cm).

```html
<!DOCTYPE html>
<html lang="en">
<head>
<meta charset="utf-8">
<title>Verdan Construction 2025 Calendar</title>
<link href="https://fonts.googleapis.com/css2?family=Montserrat:wght@400;600;800;900&display=swap" rel="stylesheet">
<style>
:root{
  --green:#1db84a;
  --green-dark:#0f8a35;
  --ink:#0d1f12;
  --black:#111;
  --paper:#fff;
  --bg:#f2f3f1;
  --rule:#c8cec9;
}
*{box-sizing:border-box;margin:0;padding:0}
html,body{width:793px;height:1200px;overflow:hidden;background:var(--bg);font-family:"Montserrat",Arial,sans-serif;color:var(--ink)}
.sheet{position:relative;width:793px;height:1200px}

/* brand text mark */
.brand{display:flex;align-items:center;gap:3px;font-weight:900;color:#fff;font-size:12px;letter-spacing:.5px}
.brand .dot{width:8px;height:8px;border-radius:50%;background:var(--green)}

/* cover */
.cover{position:absolute;left:119px;top:12px;width:211px;height:278px;background:var(--paper);box-shadow:0 2px 6px rgba(0,0,0,.25);overflow:hidden}
.cover-photo{position:absolute;left:0;top:0;width:100%;height:132px;background:linear-gradient(160deg,#8fb6d8 0%,#c9a46e 45%,#d86a2a 70%,#6b5a3e 100%)}
.cover-wave{position:absolute;left:0;top:104px;width:100%;height:40px}
.cover .brand{position:absolute;left:9px;top:9px;font-size:12px}
.cover-year{position:absolute;right:12px;top:140px;font-weight:900;font-size:20px}
.cover-name{position:absolute;left:12px;top:168px;font-weight:800;font-size:10.5px}
.cover-bar{position:absolute;left:12px;right:12px;top:185px;height:13px;background:var(--green);color:#fff;font-size:6px;font-weight:800;letter-spacing:.3px;line-height:13px;padding-left:5px;white-space:nowrap}
.cover-contacts{position:absolute;left:12px;top:206px;font-size:5.5px;line-height:9px}
.cover-tagline{position:absolute;left:12px;top:240px;font-size:6.5px;font-weight:800;letter-spacing:.4px}
.cover-foot{position:absolute;left:0;bottom:0;width:100%;height:12px;background:var(--green)}

/* month pages */
.month{position:absolute;width:182px;height:288px;background:var(--paper);box-shadow:0 2px 6px rgba(0,0,0,.22);overflow:hidden}
.col1{left:10px}.col2{left:206px}.col3{left:402px}.col4{left:597px}
.row1{top:300px}.row2{top:603px}.row3{top:904px}
.month-photo{position:absolute;left:0;top:0;width:100%;height:118px}
.month-wave{position:absolute;left:0;top:92px;width:100%;height:42px}
.month .brand{position:absolute;left:8px;top:7px;font-size:11px}
.month-year{position:absolute;right:10px;top:112px;font-weight:900;font-size:15px}
.month-name{position:absolute;left:8px;top:136px;font-weight:800;font-size:9px;letter-spacing:.6px}
.cal{position:absolute;left:8px;top:150px;width:112px}
.week,.days{display:grid;grid-template-columns:repeat(7,1fr)}
.week span{background:var(--green);color:#fff;font-size:5.5px;font-weight:800;text-align:center;line-height:9px}
.days i{font-style:normal;font-size:6px;font-weight:600;text-align:center;line-height:13px;border-bottom:1px solid #e3e6e3}
.s1 i:first-child{grid-column-start:1}.s2 i:first-child{grid-column-start:2}.s3 i:first-child{grid-column-start:3}
.s4 i:first-child{grid-column-start:4}.s5 i:first-child{grid-column-start:5}.s6 i:first-child{grid-column-start:6}.s7 i:first-child{grid-column-start:7}
.minis{position:absolute;left:125px;top:136px;width:50px}
.mini{margin-bottom:10px}
.mini b{display:block;font-size:5px;font-weight:800;letter-spacing:.3px;margin-bottom:2px;white-space:nowrap}
.mini-grid{height:40px;background:repeating-linear-gradient(to bottom,var(--rule) 0 1px,transparent 1px 7px);border-top:5px solid var(--green)}
.month-foot{position:absolute;left:0;bottom:0;width:100%;height:26px;background:var(--black);display:flex;align-items:center;gap:8px;padding:0 8px}
.month-foot .brand{position:static;font-size:8px}
.foot-info{display:flex;gap:6px;font-size:4.5px;color:#dfe5e0;white-space:nowrap}
.foot-info span::before{content:"";display:inline-block;width:4px;height:4px;border-radius:50%;background:var(--green);margin-right:2px;vertical-align:middle}
</style>
</head>
<body>
<main class="sheet">

<section class="cover">
  <div class="cover-photo" role="img" aria-label="Orange excavator working on a road construction site under a blue sky"></div>
  <svg class="cover-wave" viewBox="0 0 211 40" preserveAspectRatio="none"><path d="M0 14 Q105 -5 211 11 L211 40 L0 40Z" fill="#1db84a"/><path d="M0 24 Q105 8 211 21 L211 40 L0 40Z" fill="#fff"/></svg>
  <div class="brand"><span class="dot"></span>VERDAN</div>
  <div class="cover-year">2025</div>
  <h1 class="cover-name">Verdan Construction Limited</h1>
  <div class="cover-bar">CIVIL ENGINEERING CONSTRUCTION FIRM</div>
  <div class="cover-contacts">+1 555 0142<br>info@verdanbuild.com<br>12 Harbor Road</div>
  <div class="cover-tagline">BUILDING ROADS THAT LAST</div>
  <div class="cover-foot"></div>
</section>

<section class="month col1 row1">
  <div class="month-photo" role="img" aria-label="Construction team in hard hats and safety vests at a site event" style="background:linear-gradient(170deg,#9cc0dc,#e6c26a 55%,#3f6f3a)"></div>
  <svg class="month-wave" viewBox="0 0 182 42" preserveAspectRatio="none"><path d="M0 12 Q90 -4 182 10 L182 42 L0 42Z" fill="#1db84a"/><path d="M0 24 Q90 8 182 20 L182 42 L0 42Z" fill="#fff"/></svg>
  <div class="brand"><span class="dot"></span>VERDAN</div>
  <div class="month-year">2025</div><h2 class="month-name">JANUARY</h2>
  <div class="cal"><div class="week"><span>S</span><span>M</span><span>T</span><span>W</span><span>T</span><span>F</span><span>S</span></div>
  <div class="days s4"><i>1</i><i>2</i><i>3</i><i>4</i><i>5</i><i>6</i><i>7</i><i>8</i><i>9</i><i>10</i><i>11</i><i>12</i><i>13</i><i>14</i><i>15</i><i>16</i><i>17</i><i>18</i><i>19</i><i>20</i><i>21</i><i>22</i><i>23</i><i>24</i><i>25</i><i>26</i><i>27</i><i>28</i><i>29</i><i>30</i><i>31</i></div></div>
  <div class="minis"><div class="mini"><b>DECEMBER</b><div class="mini-grid"></div></div><div class="mini"><b>FEBRUARY</b><div class="mini-grid"></div></div></div>
  <footer class="month-foot"><div class="brand"><span class="dot"></span>VERDAN</div><div class="foot-info"><span>+1 555 0142</span><span>info@verdanbuild.com</span></div></footer>
</section>

<section class="month col2 row1">
  <div class="month-photo" role="img" aria-label="Aerial view of a paved highway with lane markings" style="background:linear-gradient(170deg,#6f8a6a,#5a5f63 50%,#8a9a7a)"></div>
  <svg class="month-wave" viewBox="0 0 182 42" preserveAspectRatio="none"><path d="M0 12 Q90 -4 182 10 L182 42 L0 42Z" fill="#1db84a"/><path d="M0 24 Q90 8 182 20 L182 42 L0 42Z" fill="#fff"/></svg>
  <div class="brand"><span class="dot"></span>VERDAN</div>
  <div class="month-year">2025</div><h2 class="month-name">FEBRUARY</h2>
  <div class="cal"><div class="week"><span>S</span><span>M</span><span>T</span><span>W</span><span>T</span><span>F</span><span>S</span></div>
  <div class="days s7"><i>1</i><i>2</i><i>3</i><i>4</i><i>5</i><i>6</i><i>7</i><i>8</i><i>9</i><i>10</i><i>11</i><i>12</i><i>13</i><i>14</i><i>15</i><i>16</i><i>17</i><i>18</i><i>19</i><i>20</i><i>21</i><i>22</i><i>23</i><i>24</i><i>25</i><i>26</i><i>27</i><i>28</i></div></div>
  <div class="minis"><div class="mini"><b>JANUARY</b><div class="mini-grid"></div></div><div class="mini"><b>MARCH</b><div class="mini-grid"></div></div></div>
  <footer class="month-foot"><div class="brand"><span class="dot"></span>VERDAN</div><div class="foot-info"><span>+1 555 0142</span><span>info@verdanbuild.com</span></div></footer>
</section>

<section class="month col3 row1">
  <div class="month-photo" role="img" aria-label="Aerial view of a new road through a residential area" style="background:linear-gradient(170deg,#a9c3d8,#7d8c7a 45%,#5c6260)"></div>
  <svg class="month-wave" viewBox="0 0 182 42" preserveAspectRatio="none"><path d="M0 12 Q90 -4 182 10 L182 42 L0 42Z" fill="#1db84a"/><path d="M0 24 Q90 8 182 20 L182 42 L0 42Z" fill="#fff"/></svg>
  <div class="brand"><span class="dot"></span>VERDAN</div>
  <div class="month-year">2025</div><h2 class="month-name">MARCH</h2>
  <div class="cal"><div class="week"><span>S</span><span>M</span><span>T</span><span>W</span><span>T</span><span>F</span><span>S</span></div>
  <div class="days s7"><i>1</i><i>2</i><i>3</i><i>4</i><i>5</i><i>6</i><i>7</i><i>8</i><i>9</i><i>10</i><i>11</i><i>12</i><i>13</i><i>14</i><i>15</i><i>16</i><i>17</i><i>18</i><i>19</i><i>20</i><i>21</i><i>22</i><i>23</i><i>24</i><i>25</i><i>26</i><i>27</i><i>28</i><i>29</i><i>30</i><i>31</i></div></div>
  <div class="minis"><div class="mini"><b>FEBRUARY</b><div class="mini-grid"></div></div><div class="mini"><b>APRIL</b><div class="mini-grid"></div></div></div>
  <footer class="month-foot"><div class="brand"><span class="dot"></span>VERDAN</div><div class="foot-info"><span>+1 555 0142</span><span>info@verdanbuild.com</span></div></footer>
</section>

<section class="month col4 row1">
  <div class="month-photo" role="img" aria-label="Road paving machine laying fresh asphalt" style="background:linear-gradient(170deg,#b4cde0,#6f8f58 45%,#4a4d50)"></div>
  <svg class="month-wave" viewBox="0 0 182 42" preserveAspectRatio="none"><path d="M0 12 Q90 -4 182 10 L182 42 L0 42Z" fill="#1db84a"/><path d="M0 24 Q90 8 182 20 L182 42 L0 42Z" fill="#fff"/></svg>
  <div class="brand"><span class="dot"></span>VERDAN</div>
  <div class="month-year">2025</div><h2 class="month-name">APRIL</h2>
  <div class="cal"><div class="week"><span>S</span><span>M</span><span>T</span><span>W</span><span>T</span><span>F</span><span>S</span></div>
  <div class="days s3"><i>1</i><i>2</i><i>3</i><i>4</i><i>5</i><i>6</i><i>7</i><i>8</i><i>9</i><i>10</i><i>11</i><i>12</i><i>13</i><i>14</i><i>15</i><i>16</i><i>17</i><i>18</i><i>19</i><i>20</i><i>21</i><i>22</i><i>23</i><i>24</i><i>25</i><i>26</i><i>27</i><i>28</i><i>29</i><i>30</i></div></div>
  <div class="minis"><div class="mini"><b>MARCH</b><div class="mini-grid"></div></div><div class="mini"><b>MAY</b><div class="mini-grid"></div></div></div>
  <footer class="month-foot"><div class="brand"><span class="dot"></span>VERDAN</div><div class="foot-info"><span>+1 555 0142</span><span>info@verdanbuild.com</span></div></footer>
</section>

<section class="month col1 row2">
  <div class="month-photo" role="img" aria-label="Aerial view of a road junction among green fields" style="background:linear-gradient(170deg,#5f8a4a,#7a6a4a 50%,#4d6a3a)"></div>
  <svg class="month-wave" viewBox="0 0 182 42" preserveAspectRatio="none"><path d="M0 12 Q90 -4 182 10 L182 42 L0 42Z" fill="#1db84a"/><path d="M0 24 Q90 8 182 20 L182 42 L0 42Z" fill="#fff"/></svg>
  <div class="brand"><span class="dot"></span>VERDAN</div>
  <div class="month-year">2025</div><h2 class="month-name">MAY</h2>
  <div class="cal"><div class="week"><span>S</span><span>M</span><span>T</span><span>W</span><span>T</span><span>F</span><span>S</span></div>
  <div class="days s5"><i>1</i><i>2</i><i>3</i><i>4</i><i>5</i><i>6</i><i>7</i><i>8</i><i>9</i><i>10</i><i>11</i><i>12</i><i>13</i><i>14</i><i>15</i><i>16</i><i>17</i><i>18</i><i>19</i><i>20</i><i>21</i><i>22</i><i>23</i><i>24</i><i>25</i><i>26</i><i>27</i><i>28</i><i>29</i><i>30</i><i>31</i></div></div>
  <div class="minis"><div class="mini"><b>APRIL</b><div class="mini-grid"></div></div><div class="mini"><b>JUNE</b><div class="mini-grid"></div></div></div>
  <footer class="month-foot"><div class="brand"><span class="dot"></span>VERDAN</div><div class="foot-info"><span>+1 555 0142</span><span>info@verdanbuild.com</span></div></footer>
</section>

<section class="month col2 row2">
  <div class="month-photo" role="img" aria-label="Wide freshly paved road surface" style="background:linear-gradient(170deg,#c4d6e4,#8c9184 45%,#55595c)"></div>
  <svg class="month-wave" viewBox="0 0 182 42" preserveAspectRatio="none"><path d="M0 12 Q90 -4 182 10 L182 42 L0 42Z" fill="#1db84a"/><path d="M0 24 Q90 8 182 20 L182 42 L0 42Z" fill="#fff"/></svg>
  <div class="brand"><span class="dot"></span>VERDAN</div>
  <div class="month-year">2025</div><h2 class="month-name">JUNE</h2>
  <div class="cal"><div class="week"><span>S</span><span>M</span><span>T</span><span>W</span><span>T</span><span>F</span><span>S</span></div>
  <div class="days s1"><i>1</i><i>2</i><i>3</i><i>4</i><i>5</i><i>6</i><i>7</i><i>8</i><i>9</i><i>10</i><i>11</i><i>12</i><i>13</i><i>14</i><i>15</i><i>16</i><i>17</i><i>18</i><i>19</i><i>20</i><i>21</i><i>22</i><i>23</i><i>24</i><i>25</i><i>26</i><i>27</i><i>28</i><i>29</i><i>30</i></div></div>
  <div class="minis"><div class="mini"><b>MAY</b><div class="mini-grid"></div></div><div class="mini"><b>JULY</b><div class="mini-grid"></div></div></div>
  <footer class="month-foot"><div class="brand"><span class="dot"></span>VERDAN</div><div class="foot-info"><span>+1 555 0142</span><span>info@verdanbuild.com</span></div></footer>
</section>

<section class="month col3 row2">
  <div class="month-photo" role="img" aria-label="Road with curbs and red earth verges under construction" style="background:linear-gradient(170deg,#b9cfe0,#a66a3e 50%,#5b5d5f)"></div>
  <svg class="month-wave" viewBox="0 0 182 42" preserveAspectRatio="none"><path d="M0 12 Q90 -4 182 10 L182 42 L0 42Z" fill="#1db84a"/><path d="M0 24 Q90 8 182 20 L182 42 L0 42Z" fill="#fff"/></svg>
  <div class="brand"><span class="dot"></span>VERDAN</div>
  <div class="month-year">2025</div><h2 class="month-name">JULY</h2>
  <div class="cal"><div class="week"><span>S</span><span>M</span><span>T</span><span>W</span><span>T</span><span>F</span><span>S</span></div>
  <div class="days s3"><i>1</i><i>2</i><i>3</i><i>4</i><i>5</i><i>6</i><i>7</i><i>8</i><i>9</i><i>10</i><i>11</i><i>12</i><i>13</i><i>14</i><i>15</i><i>16</i><i>17</i><i>18</i><i>19</i><i>20</i><i>21</i><i>22</i><i>23</i><i>24</i><i>25</i><i>26</i><i>27</i><i>28</i><i>29</i><i>30</i><i>31</i></div></div>
  <div class="minis"><div class="mini"><b>JUNE</b><div class="mini-grid"></div></div><div class="mini"><b>AUGUST</b><div class="mini-grid"></div></div></div>
  <footer class="month-foot"><div class="brand"><span class="dot"></span>VERDAN</div><div class="foot-info"><span>+1 555 0142</span><span>info@verdanbuild.com</span></div></footer>
</section>

<section class="month col4 row2">
  <div class="month-photo" role="img" aria-label="Asphalt paver and roller working on a road" style="background:linear-gradient(170deg,#c6d8e6,#6e7a6c 45%,#3e4144)"></div>
  <svg class="month-wave" viewBox="0 0 182 42" preserveAspectRatio="none"><path d="M0 12 Q90 -4 182 10 L182 42 L0 42Z" fill="#1db84a"/><path d="M0 24 Q90 8 182 20 L182 42 L0 42Z" fill="#fff"/></svg>
  <div class="brand"><span class="dot"></span>VERDAN</div>
  <div class="month-year">2025</div><h2 class="month-name">AUGUST</h2>
  <div class="cal"><div class="week"><span>S</span><span>M</span><span>T</span><span>W</span><span>T</span><span>F</span><span>S</span></div>
  <div class="days s6"><i>1</i><i>2</i><i>3</i><i>4</i><i>5</i><i>6</i><i>7</i><i>8</i><i>9</i><i>10</i><i>11</i><i>12</i><i>13</i><i>14</i><i>15</i><i>16</i><i>17</i><i>18</i><i>19</i><i>20</i><i>21</i><i>22</i><i>23</i><i>24</i><i>25</i><i>26</i><i>27</i><i>28</i><i>29</i><i>30</i><i>31</i></div></div>
  <div class="minis"><div class="mini"><b>JULY</b><div class="mini-grid"></div></div><div class="mini"><b>SEPTEMBER</b><div class="mini-grid"></div></div></div>
  <footer class="month-foot"><div class="brand"><span class="dot"></span>VERDAN</div><div class="foot-info"><span>+1 555 0142</span><span>info@verdanbuild.com</span></div></footer>
</section>

<section class="month col1 row3">
  <div class="month-photo" role="img" aria-label="Row of construction trucks parked at a yard" style="background:linear-gradient(170deg,#b7cde0,#d0d4d6 45%,#6a6f6a)"></div>
  <svg class="month-wave" viewBox="0 0 182 42" preserveAspectRatio="none"><path d="M0 12 Q90 -4 182 10 L182 42 L0 42Z" fill="#1db84a"/><path d="M0 24 Q90 8 182 20 L182 42 L0 42Z" fill="#fff"/></svg>
  <div class="brand"><span class="dot"></span>VERDAN</div>
  <div class="month-year">2025</div><h2 class="month-name">SEPTEMBER</h2>
  <div class="cal"><div class="week"><span>S</span><span>M</span><span>T</span><span>W</span><span>T</span><span>F</span><span>S</span></div>
  <div class="days s2"><i>1</i><i>2</i><i>3</i><i>4</i><i>5</i><i>6</i><i>7</i><i>8</i><i>9</i><i>10</i><i>11</i><i>12</i><i>13</i><i>14</i><i>15</i><i>16</i><i>17</i><i>18</i><i>19</i><i>20</i><i>21</i><i>22</i><i>23</i><i>24</i><i>25</i><i>26</i><i>27</i><i>28</i><i>29</i><i>30</i></div></div>
  <div class="minis"><div class="mini"><b>AUGUST</b><div class="mini-grid"></div></div><div class="mini"><b>OCTOBER</b><div class="mini-grid"></div></div></div>
  <footer class="month-foot"><div class="brand"><span class="dot"></span>VERDAN</div><div class="foot-info"><span>+1 555 0142</span><span>info@verdanbuild.com</span></div></footer>
</section>

<section class="month col2 row3">
  <div class="month-photo" role="img" aria-label="Aerial view of a red earth road cut through green bush" style="background:linear-gradient(170deg,#4f7a3e,#b0582e 50%,#4a6e38)"></div>
  <svg class="month-wave" viewBox="0 0 182 42" preserveAspectRatio="none"><path d="M0 12 Q90 -4 182 10 L182 42 L0 42Z" fill="#1db84a"/><path d="M0 24 Q90 8 182 20 L182 42 L0 42Z" fill="#fff"/></svg>
  <div class="brand"><span class="dot"></span>VERDAN</div>
  <div class="month-year">2025</div><h2 class="month-name">OCTOBER</h2>
  <div class="cal"><div class="week"><span>S</span><span>M</span><span>T</span><span>W</span><span>T</span><span>F</span><span>S</span></div>
  <div class="days s4"><i>1</i><i>2</i><i>3</i><i>4</i><i>5</i><i>6</i><i>7</i><i>8</i><i>9</i><i>10</i><i>11</i><i>12</i><i>13</i><i>14</i><i>15</i><i>16</i><i>17</i><i>18</i><i>19</i><i>20</i><i>21</i><i>22</i><i>23</i><i>24</i><i>25</i><i>26</i><i>27</i><i>28</i><i>29</i><i>30</i><i>31</i></div></div>
  <div class="minis"><div class="mini"><b>SEPTEMBER</b><div class="mini-grid"></div></div><div class="mini"><b>NOVEMBER</b><div class="mini-grid"></div></div></div>
  <footer class="month-foot"><div class="brand"><span class="dot"></span>VERDAN</div><div class="foot-info"><span>+1 555 0142</span><span>info@verdanbuild.com</span></div></footer>
</section>

<section class="month col3 row3">
  <div class="month-photo" role="img" aria-label="Aerial view of a paved parking area with markings" style="background:linear-gradient(170deg,#9aa39a,#c9ccc8 50%,#7f877c)"></div>
  <svg class="month-wave" viewBox="0 0 182 42" preserveAspectRatio="none"><path d="M0 12 Q90 -4 182 10 L182 42 L0 42Z" fill="#1db84a"/><path d="M0 24 Q90 8 182 20 L182 42 L0 42Z" fill="#fff"/></svg>
  <div class="brand"><span class="dot"></span>VERDAN</div>
  <div class="month-year">2025</div><h2 class="month-name">NOVEMBER</h2>
  <div class="cal"><div class="week"><span>S</span><span>M</span><span>T</span><span>W</span><span>T</span><span>F</span><span>S</span></div>
  <div class="days s7"><i>1</i><i>2</i><i>3</i><i>4</i><i>5</i><i>6</i><i>7</i><i>8</i><i>9</i><i>10</i><i>11</i><i>12</i><i>13</i><i>14</i><i>15</i><i>16</i><i>17</i><i>18</i><i>19</i><i>20</i><i>21</i><i>22</i><i>23</i><i>24</i><i>25</i><i>26</i><i>27</i><i>28</i><i>29</i><i>30</i></div></div>
  <div class="minis"><div class="mini"><b>OCTOBER</b><div class="mini-grid"></div></div><div class="mini"><b>DECEMBER</b><div class="mini-grid"></div></div></div>
  <footer class="month-foot"><div class="brand"><span class="dot"></span>VERDAN</div><div class="foot-info"><span>+1 555 0142</span><span>info@verdanbuild.com</span></div></footer>
</section>

<section class="month col4 row3">
  <div class="month-photo" role="img" aria-label="Fleet of white construction trucks lined up" style="background:linear-gradient(170deg,#b9d0e2,#e4e6e4 50%,#6f756f)"></div>
  <svg class="month-wave" viewBox="0 0 182 42" preserveAspectRatio="none"><path d="M0 12 Q90 -4 182 10 L182 42 L0 42Z" fill="#1db84a"/><path d="M0 24 Q90 8 182 20 L182 42 L0 42Z" fill="#fff"/></svg>
  <div class="brand"><span class="dot"></span>VERDAN</div>
  <div class="month-year">2025</div><h2 class="month-name">DECEMBER</h2>
  <div class="cal"><div class="week"><span>S</span><span>M</span><span>T</span><span>W</span><span>T</span><span>F</span><span>S</span></div>
  <div class="days s2"><i>1</i><i>2</i><i>3</i><i>4</i><i>5</i><i>6</i><i>7</i><i>8</i><i>9</i><i>10</i><i>11</i><i>12</i><i>13</i><i>14</i><i>15</i><i>16</i><i>17</i><i>18</i><i>19</i><i>20</i><i>21</i><i>22</i><i>23</i><i>24</i><i>25</i><i>26</i><i>27</i><i>28</i><i>29</i><i>30</i><i>31</i></div></div>
  <div class="minis"><div class="mini"><b>NOVEMBER</b><div class="mini-grid"></div></div><div class="mini"><b>JANUARY</b><div class="mini-grid"></div></div></div>
  <footer class="month-foot"><div class="brand"><span class="dot"></span>VERDAN</div><div class="foot-info"><span>+1 555 0142</span><span>info@verdanbuild.com</span></div></footer>
</section>

</main>
</body>
</html>
```